Mirvanto general construction

We need an website that are similar to these websites:
https://www.dulcemor.com/en/
https://pomvilo.com/company/

but with a tweak. Do not copy the entire website but atleast similar and yet better than them.

For reference this our current website.
https://mirvanto.ph/

For the winning Designer please help us with the migration from our old website to the new redesign website.

```html
<!DOCTYPE html>
<html lang="en">
<head>
<meta charset="utf-8">
<title>Mirvanto — General Construction</title>
<link href="https://fonts.googleapis.com/css2?family=Inter:wght@300;400;500;600;700&display=swap" rel="stylesheet">
<style>
:root{
  --orange:#f5821f;
  --orange-soft:#fde3cc;
  --navy:#1f2b3e;
  --navy-deep:#18222f;
  --ink:#1c1c1c;
  --muted:#6b6b6b;
  --line:#e3e3e3;
  --panel:#f4f4f4;
  --white:#ffffff;
}
*{margin:0;padding:0;box-sizing:border-box}
html,body{width:1200px;height:3798px;overflow:hidden}
body{font-family:'Inter',sans-serif;color:var(--ink);background:var(--white);position:relative}
.abs{position:absolute}
.arrow-box{display:flex;align-items:center;justify-content:center}
.arrow-box svg{width:14px;height:14px}

/* top bar */
.topbar{left:0;top:0;width:1200px;height:41px;background:var(--navy)}
.topbar-accent{left:850px;top:0;width:350px;height:41px;background:var(--orange);clip-path:polygon(16px 0,100% 0,100% 100%,0 100%)}
.topbar-phone{left:128px;top:12px;color:var(--white);font-size:12px;font-weight:500;display:flex;gap:6px;align-items:center}
.social{top:9px;width:23px;height:23px;border-radius:50%;background:var(--white)}

/* nav */
.nav{left:0;top:41px;width:1200px;height:81px;background:var(--white)}
.brand{left:125px;top:66px;display:flex;align-items:center;gap:8px;font-size:17px;font-weight:700;color:var(--orange)}
.brand-dot{width:14px;height:14px;border-radius:50%;background:var(--orange)}
.nav-link{top:74px;font-size:13px;color:var(--ink)}
.btn-quote{left:933px;top:60px;width:142px;height:45px;background:var(--orange);color:var(--white);font-size:12px;font-weight:600;display:flex;align-items:center;padding-left:15px}
.btn-quote .arrow-box{position:absolute;right:8px;top:9px;width:28px;height:27px;background:var(--white)}

/* hero */
.hero{left:0;top:122px;width:1200px;height:589px;background:linear-gradient(180deg,#2b3a52 0%,#4a4c56 35%,#8b6a3d 60%,#2a2a33 100%)}
.hero-shade{left:0;top:122px;width:1200px;height:589px;background:linear-gradient(90deg,rgba(20,26,38,.55),rgba(20,26,38,0) 60%)}
.hero-tab{left:125px;top:237px;width:117px;height:359px;background:var(--orange)}
.hero-eyebrow{left:152px;top:313px;color:var(--white);font-size:14px;letter-spacing:3px;font-weight:500}
.hero-title{left:152px;top:352px;color:var(--white);font-size:44px;line-height:52px;font-weight:400}
.hero-title strong{font-weight:700}
.hero-btn{left:152px;top:478px;width:150px;height:44px;background:var(--white);font-size:12px;display:flex;align-items:center;padding-left:18px;border:3px solid var(--white)}
.hero-btn .arrow-box{position:absolute;right:3px;top:3px;width:36px;height:32px;background:var(--navy)}
.slide-card{left:774px;top:646px;width:301px;height:166px;background:var(--white);box-shadow:0 8px 24px rgba(0,0,0,.12)}
.slide-head{left:0;top:0;width:301px;height:48px;background:var(--navy);color:var(--orange);font-size:11px;letter-spacing:2.5px;font-weight:600;padding:18px 25px}
.slide-count{position:absolute;right:26px;top:12px;color:var(--orange);font-size:20px;letter-spacing:0}
.slide-count span{color:#8a93a3;font-size:15px}
.slide-title{left:25px;top:64px;font-size:23px;line-height:29px;font-weight:500}
.slide-card .arrow-box{position:absolute;left:228px;top:98px;width:46px;height:46px;background:var(--orange)}

/* stats */
.stat{top:754px}
.stat-num{font-size:30px;font-weight:500}
.stat-label{font-size:14px;color:#444;margin-top:2px}
.stat-sep{top:760px;width:2px;height:52px;background:var(--orange)}

/* about */
.about-photo{left:0;top:905px;width:500px;height:489px;background:linear-gradient(180deg,#5f8fc4 0%,#8fb4d8 45%,#d0a03d 60%,#1c4f86 80%,#163f6c 100%)}
.exp-box{left:351px;top:1228px;width:149px;height:166px;background:var(--navy);color:var(--white);padding:28px 24px}
.exp-num{font-size:64px;font-weight:500;line-height:64px}
.exp-label{font-size:13px;line-height:16px;margin-top:10px}
.about-title{left:551px;top:934px;width:540px;font-size:34px;line-height:45px;font-weight:600}
.about-text{left:551px;top:1044px;width:530px;font-size:14px;line-height:25px;color:#555}
.btn-orange{background:var(--orange);color:var(--white);font-size:12px;font-weight:500;display:flex;align-items:center;padding-left:17px}
.about-btn{left:551px;top:1141px;width:187px;height:44px}
.btn-orange .arrow-box{position:absolute;right:6px;top:6px;width:32px;height:32px;background:var(--white)}
.about-panel{left:500px;top:1228px;width:437px;height:166px;background:var(--panel)}
.about-divider{left:718px;top:1250px;width:1px;height:120px;background:var(--line)}
.mini{top:1252px;width:170px}
.mini-icon{width:40px;height:40px;background:var(--orange-soft);display:flex;align-items:center;justify-content:center}
.mini h4{font-size:15px;font-weight:500;margin-top:14px}
.mini p{font-size:10px;line-height:13px;color:#777;margin-top:8px}

/* expertise */
.eyebrow{color:var(--orange);font-size:16px}
.section-head{left:0;width:1200px;text-align:center}
.section-title{font-size:34px;font-weight:600}
.section-text{font-size:14px;line-height:25px;color:#555;width:700px;margin:0 auto}
.card{width:282px;height:272px;background:var(--white);box-shadow:0 4px 18px rgba(0,0,0,.07);padding:24px 24px 0}
.card.active{background:var(--orange);color:var(--white)}
.card svg.icon{width:46px;height:50px}
.card h3{font-size:15px;font-weight:500;line-height:19px;margin-top:14px;height:40px;display:flex;align-items:flex-start}
.card hr{border:0;border-top:1px solid var(--line);margin:10px 0 16px}
.card.active hr{border-color:rgba(255,255,255,.45)}
.card p{font-size:10px;line-height:16.5px;color:#666}
.card.active p{color:var(--white)}
.card .arrow-box{position:absolute;left:24px;bottom:0;width:46px;height:46px;background:var(--orange)}
.card.active .arrow-box{background:var(--white)}

/* banner */
.banner{left:125px;top:2333px;width:950px;height:348px;background:linear-gradient(180deg,#6d7079 0%,#4b4e57 45%,#2a2c33 100%)}
.banner-eyebrow{left:178px;top:2390px;color:var(--white);font-size:16px}
.banner-title{left:178px;top:2422px;color:var(--white);font-size:35px;font-weight:600}
.banner-text{left:178px;top:2475px;width:540px;color:#eee;font-size:15px;line-height:25px}
.quote-form{left:267px;top:2610px;width:808px;height:143px;background:var(--orange);padding:25px 25px}
.quote-form h3{color:var(--white);font-size:19px;font-weight:600}
.field{position:absolute;top:80px;width:198px}
.field label{display:block;color:var(--white);font-size:11px;margin-bottom:6px}
.field .input{height:37px;background:var(--white);font-size:10px;color:#aaa;padding:12px;display:flex;align-items:center;justify-content:space-between}
.form-submit{position:absolute;left:650px;top:2693px;width:133px;height:37px;background:var(--navy);color:var(--white);font-size:11px;display:flex;align-items:center;justify-content:center}

/* news */
.news-title{left:125px;top:2895px;font-size:34px;font-weight:600}
.view-all{left:948px;top:2870px;width:127px;height:43px}
.news-big{left:125px;top:2969px;width:431px;height:467px;background:var(--panel);padding:14px}
.news-big .photo{width:403px;height:269px;background:linear-gradient(180deg,#3c4660 0%,#7a6a72 55%,#2a2b35 100%)}
.meta{font-size:13px;display:flex;align-items:center;gap:14px}
.meta .cat{color:var(--orange)}
.meta .dot{width:8px;height:8px;border-radius:50%;background:var(--ink)}
.news-big h3{font-size:22px;font-weight:500;line-height:27px;margin-top:12px}
.news-big p{font-size:10px;line-height:16px;color:#666;margin-top:14px}
.news-row{left:575px;width:500px;height:143px;background:var(--panel);padding:14px}
.news-row .thumb{position:absolute;left:14px;top:14px;width:130px;height:115px}
.news-row .body{position:absolute;left:165px;top:44px;width:300px}
.news-row h4{font-size:15px;font-weight:500;line-height:19px;margin-top:14px}

/* footer */
.footer{left:0;top:3530px;width:1200px;height:268px;background:var(--navy);color:#c9ced6}
.foot-brand{left:165px;top:3580px;display:flex;align-items:center;gap:6px;color:var(--white);font-size:12px;font-weight:700}
.foot-about{left:165px;top:3612px;width:175px;font-size:11px;line-height:13px;color:#9aa3b0}
.foot-h{font-size:12px;color:var(--white);font-weight:500}
.foot-link{font-size:12px;color:#9aa3b0}
.foot-news{left:880px;top:3648px;width:155px;height:34px;border-radius:17px;background:#2c3a50;font-size:11px;color:#9aa3b0;padding:11px 14px}
.foot-send{left:1002px;top:3652px;width:27px;height:27px;border-radius:50%;background:var(--orange)}
.foot-bottom{top:3775px;font-size:11px;color:#9aa3b0}
</style>
</head>
<body>

<!-- top bar -->
<div class="abs topbar"></div>
<div class="abs topbar-accent"></div>
<div class="abs topbar-phone">
  <svg width="12" height="12" viewBox="0 0 24 24" fill="#fff"><path d="M6.6 10.8a15 15 0 0 0 6.6 6.6l2.2-2.2a1 1 0 0 1 1-.25 11.4 11.4 0 0 0 3.6.57 1 1 0 0 1 1 1V20a1 1 0 0 1-1 1A17 17 0 0 1 3 4a1 1 0 0 1 1-1h3.5a1 1 0 0 1 1 1c0 1.25.2 2.45.57 3.57a1 1 0 0 1-.25 1z"/></svg>
  +63 (0) 55 210-4837
</div>
<div class="abs social" style="left:977px" aria-label="Social link"></div>
<div class="abs social" style="left:1014px" aria-label="Social link"></div>
<div class="abs social" style="left:1051px" aria-label="Email"></div>

<!-- nav -->
<div class="abs nav"></div>
<div class="abs brand"><span class="brand-dot"></span>Mirvanto</div>
<div class="abs nav-link" style="left:280px">Home</div>
<div class="abs nav-link" style="left:360px">About Us</div>
<div class="abs nav-link" style="left:460px">Our Services</div>
<div class="abs nav-link" style="left:585px">Our Team</div>
<div class="abs nav-link" style="left:688px">News &amp; Media</div>
<div class="abs nav-link" style="left:821px">Contact Us</div>
<div class="abs btn-quote">Get A Quote
  <span class="arrow-box"><svg viewBox="0 0 14 14" fill="none" stroke="#1c1c1c" stroke-width="1.4"><path d="M3 11L11 3M5 3h6v6"/></svg></span>
</div>

<!-- hero -->
<div class="abs hero" role="img" aria-label="Refinery towers lit at dusk with a flare and steam clouds"></div>
<div class="abs hero-shade"></div>
<div class="abs hero-tab"></div>
<div class="abs hero-eyebrow">— WELCOME TO MIRVANTO</div>
<h1 class="abs hero-title">Delivering Solutions.<br><strong>Powering Progress.</strong></h1>
<div class="abs hero-btn">Our Services
  <span class="arrow-box"><svg viewBox="0 0 14 14" fill="none" stroke="#f5821f" stroke-width="1.4"><path d="M3 11L11 3M5 3h6v6"/></svg></span>
</div>
<div class="abs slide-card">
  <div class="abs slide-head">MANUFACTURING<span class="slide-count">01<span>/03</span></span></div>
  <div class="abs slide-title">Customized<br>manufacturing<br>solution</div>
  <span class="arrow-box"><svg viewBox="0 0 14 14" fill="none" stroke="#fff" stroke-width="1.4"><path d="M3 11L11 3M5 3h6v6"/></svg></span>
</div>

<!-- stats -->
<div class="abs stat" style="left:125px"><div class="stat-num">65,000+</div><div class="stat-label">Employees</div></div>
<div class="abs stat-sep" style="left:287px"></div>
<div class="abs stat" style="left:340px"><div class="stat-num">50+</div><div class="stat-label">Countries</div></div>
<div class="abs stat-sep" style="left:458px"></div>
<div class="abs stat" style="left:510px"><div class="stat-num">120+</div><div class="stat-label">Subsidiaries</div></div>

<!-- about -->
<div class="abs about-photo" role="img" aria-label="Offshore oil platform with yellow steel structure over blue sea"></div>
<div class="abs exp-box"><div class="exp-num">32</div><div class="exp-label">Year of<br>Experience</div></div>
<h2 class="abs about-title">Engineering Confidence for the Oil &amp; Gas Industry</h2>
<p class="abs about-text">From offshore platforms to onshore facilities, we provide integrated industrial solutions backed by technical expertise, uncompromising safety standards, and a commitment to operational excellence.</p>
<div class="abs btn-orange about-btn">Get Your Free Code
  <span class="arrow-box"><svg viewBox="0 0 14 14" fill="none" stroke="#1c1c1c" stroke-width="1.4"><path d="M3 11L11 3M5 3h6v6"/></svg></span>
</div>
<div class="abs about-panel"></div>
<div class="abs about-divider"></div>
<div class="abs mini" style="left:551px">
  <div class="mini-icon"><svg width="22" height="22" viewBox="0 0 24 24" fill="none" stroke="#f5821f" stroke-width="1.4"><circle cx="12" cy="10" r="5"/><path d="M10 18h4M10 21h4M12 2v1M4 10H3M21 10h-1M6 4l1 1M18 4l-1 1"/></svg></div>
  <h4>Our Moto</h4>
  <p>Lorem Ipsum is simply dummy text of the printing and typesetting industry.</p>
</div>
<div class="abs mini" style="left:778px">
  <div class="mini-icon"><svg width="22" height="22" viewBox="0 0 24 24" fill="none" stroke="#f5821f" stroke-width="1.4"><circle cx="12" cy="12" r="8"/><circle cx="12" cy="12" r="4.5"/><circle cx="12" cy="12" r="1.5"/><path d="M12 12l7-7"/></svg></div>
  <h4>Our Goal</h4>
  <p>It is a long established fact that a reader will be content distracted</p>
</div>

<!-- expertise -->
<div class="abs section-head" style="top:1486px">
  <div class="eyebrow">Our Expertise</div>
  <h2 class="section-title" style="margin-top:12px">Delivering Excellence Across Key Sectors</h2>
  <p class="section-text" style="margin-top:14px">Our ability to deliver a quality product has given us the reputation to position ourselves as a leading contractor in the sectors and industries that we serve.</p>
</div>

<div class="abs card" style="left:125px;top:1671px">
  <svg class="icon" viewBox="0 0 46 50" fill="none" stroke="#f5821f" stroke-width="1.6"><path d="M23 3l18 6v14c0 12-8 20-18 24C13 43 5 35 5 23V9z"/><path d="M23 36V22M23 30c-6 0-8-5-8-9 5 0 8 3 8 9zM23 27c5 0 8-4 8-8-5 0-8 3-8 8z"/></svg>
  <h3>Environmental Protection and Management</h3><hr>
  <p>We process industrial solid wastes by adopting the latest technologies and convert them to energy in the form of electrical power.</p>
  <span class="arrow-box"><svg viewBox="0 0 14 14" fill="none" stroke="#fff" stroke-width="1.4"><path d="M3 11L11 3M5 3h6v6"/></svg></span>
</div>
<div class="abs card active" style="left:458px;top:1671px">
  <svg class="icon" viewBox="0 0 46 50" fill="none" stroke="#fff" stroke-width="1.6"><rect x="5" y="22" width="36" height="22"/><rect x="10" y="28" width="10" height="8"/><rect x="24" y="28" width="10" height="8"/><path d="M10 22V12h8v10M26 8a4 4 0 1 1 8 0 4 4 0 0 1-8 0M3 44h40"/></svg>
  <h3>Power Generation</h3><hr>
  <p>We are experienced in the refurbishment of utility steam raising plants, repair and maintenance of ancillary equipment from valves to pumps, with expertise in plant shutdowns and turnarounds.</p>
  <span class="arrow-box"><svg viewBox="0 0 14 14" fill="none" stroke="#f5821f" stroke-width="1.4"><path d="M3 11L11 3M5 3h6v6"/></svg></span>
</div>
<div class="abs card" style="left:793px;top:1671px">
  <svg class="icon" viewBox="0 0 46 50" fill="none" stroke="#f5821f" stroke-width="1.6"><path d="M17 14C11 24 7 30 7 35a10 10 0 0 0 20 0c0-5-4-11-10-21z"/><path d="M33 4c-3 5-5 8-5 10a5 5 0 0 0 10 0c0-2-2-5-5-10z"/></svg>
  <h3>Water Treatment</h3><hr>
  <p>We have in-house expertise in the construction of Sewage Water Treatment Plants (SWTP) and utility desalination plants for the conversion of seawater into potable water.</p>
  <span class="arrow-box"><svg viewBox="0 0 14 14" fill="none" stroke="#fff" stroke-width="1.4"><path d="M3 11L11 3M5 3h6v6"/></svg></span>
</div>
<div class="abs card" style="left:125px;top:1971px">
  <svg class="icon" viewBox="0 0 46 50" fill="none" stroke="#f5821f" stroke-width="1.6"><rect x="8" y="8" width="24" height="38"/><path d="M32 22h8v24M4 46h40M14 14h4M22 14h4M14 22h4M22 22h4M14 30h4M22 30h4M17 46v-8h6v8"/></svg>
  <h3>Construction</h3><hr>
  <p>Our experience in working to international standards and complying with international business ethics and conduct reflects our commitment to health, safety, and environmental management.</p>
  <span class="arrow-box"><svg viewBox="0 0 14 14" fill="none" stroke="#fff" stroke-width="1.4"><path d="M3 11L11 3M5 3h6v6"/></svg></span>
</div>
<div class="abs card" style="left:458px;top:1971px">
  <svg class="icon" viewBox="0 0 46 50" fill="none" stroke="#f5821f" stroke-width="1.6"><path d="M10 46L22 10l12 36M14 34h16M17 24h10M4 46h38M22 10l18-6v14M34 18v10"/></svg>
  <h3>Oil and Gas</h3><hr>
  <p>We are known in the oil and gas industry for our ability to provide multi-skilled, reliable, and cost-effective manpower.</p>
  <span class="arrow-box"><svg viewBox="0 0 14 14" fill="none" stroke="#fff" stroke-width="1.4"><path d="M3 11L11 3M5 3h6v6"/></svg></span>
</div>
<div class="abs card" style="left:793px;top:1971px">
  <svg class="icon" viewBox="0 0 46 50" fill="none" stroke="#f5821f" stroke-width="1.6"><path d="M6 34a17 17 0 0 1 34 0M3 34h40v5H3zM18 18v10M28 18v10M18 18h10"/></svg>
  <h3>Safety Excellence</h3><hr>
  <p>Safety is our core value. We are committed to achieving the highest safety standards across all our operations.</p>
  <span class="arrow-box"><svg viewBox="0 0 14 14" fill="none" stroke="#fff" stroke-width="1.4"><path d="M3 11L11 3M5 3h6v6"/></svg></span>
</div>

<!-- banner -->
<div class="abs banner" role="img" aria-label="Oil pumpjack silhouetted against a cloudy evening sky"></div>
<div class="abs banner-eyebrow">Gas &amp; Oil</div>
<h2 class="abs banner-title">Energy Infrastructure Solutions</h2>
<p class="abs banner-text">Supporting the energy sector with world-class industrial services, technical expertise, and innovative solutions that maximize performance, safety, and operational efficiency.</p>
<div class="abs quote-form">
  <h3>Get your free quote today</h3>
  <div class="field" style="left:25px"><label>Full Name*</label><div class="input">Your Name</div></div>
  <div class="field" style="left:233px"><label>Phone</label><div class="input">Your Phone No.</div></div>
  <div class="field" style="left:441px"><label>Service Type</label><div class="input">Select Your Service<svg width="8" height="6" viewBox="0 0 8 6"><path d="M0 0h8L4 6z" fill="#333"/></svg></div></div>
</div>
<div class="abs form-submit" style="left:917px">Get A Free Quote</div>

<!-- news -->
<div class="abs eyebrow" style="left:125px;top:2855px">Latest News</div>
<h2 class="abs news-title">Stay Informed With Our Latest Updates</h2>
<div class="abs btn-orange view-all">View All
  <span class="arrow-box"><svg viewBox="0 0 14 14" fill="none" stroke="#1c1c1c" stroke-width="1.4"><path d="M3 11L11 3M5 3h6v6"/></svg></span>
</div>
<div class="abs news-big">
  <div class="photo" role="img" aria-label="Offshore rig at dusk with cranes against the sky"></div>
  <div class="meta" style="margin-top:22px;padding-left:9px"><span class="cat">Manufacturing</span><span class="dot"></span><span>Jan 28, 2026</span></div>
  <h3 style="padding-left:9px">Top Manufacturing Trends Shaping Industry's Future</h3>
  <p style="padding-left:9px">Explore the latest trends transforming manufacturing and how businesses can adapt for success.</p>
</div>
<div class="abs news-row" style="top:2969px">
  <div class="thumb" role="img" aria-label="Two workers in hard hats and orange vests on site" style="background:linear-gradient(135deg,#3b4452,#d46a2c 55%,#2c3038)"></div>
  <div class="body"><div class="meta"><span class="cat">Manufacturing</span><span class="dot"></span><span>Jan 18, 2026</span></div><h4>5 Key Strategies for Efficient Industrial Operations</h4></div>
</div>
<div class="abs news-row" style="top:3131px">
  <div class="thumb" role="img" aria-label="Industrial tower under a clear blue sky" style="background:linear-gradient(180deg,#6fb2dc,#b7d2e0 60%,#7c7a6e)"></div>
  <div class="body"><div class="meta"><span class="cat">Manufacturing</span><span class="dot"></span><span>Jan 23, 2026</span></div><h4>Exploring the Future of Aerospace: What Lies Ahead?</h4></div>
</div>
<div class="abs news-row" style="top:3294px">
  <div class="thumb" role="img" aria-label="Orange robotic arms on a factory production line" style="background:linear-gradient(135deg,#2d3a4e,#d9892e 50%,#3a4456)"></div>
  <div class="body"><div class="meta"><span class="cat">Manufacturing</span><span class="dot"></span><span>feb 8, 2026</span></div><h4>Boosting Manufacturing Efficiency with Innovation</h4></div>
</div>

<!-- footer -->
<div class="abs footer"></div>
<div class="abs foot-brand"><span class="brand-dot" style="width:10px;height:10px"></span>Mirvanto</div>
<p class="abs foot-about">There are many variations of passages of Lorem Ipsum available, but the majority have suffered alteration in some form, by injected humour, or randomised</p>
<div class="abs foot-h" style="left:376px;top:3580px">Company</div>
<div class="abs foot-link" style="left:376px;top:3612px">Home</div>
<div class="abs foot-link" style="left:376px;top:3642px">News &amp; Media</div>
<div class="abs foot-link" style="left:510px;top:3612px">About Us</div>
<div class="abs foot-link" style="left:510px;top:3642px">Contact Us</div>
<div class="abs foot-link" style="left:634px;top:3612px">Our Services</div>
<div class="abs foot-link" style="left:634px;top:3642px">Our Team</div>
<div class="abs foot-h" style="left:880px;top:3580px">Stay Updated</div>
<p class="abs foot-about" style="left:880px;top:3598px;width:140px">Get the latest news and insights on lone worker safety.</p>
<div class="abs foot-news">Email</div>
<div class="abs foot-send arrow-box"><svg viewBox="0 0 14 14" fill="none" stroke="#fff" stroke-width="1.3"><path d="M2 7l10-5-4 10-1.5-4z"/></svg></div>
<div class="abs foot-bottom" style="left:165px">© 2026 MIRVANTO. All rights reserved.</div>
<div class="abs foot-bottom" style="left:757px">Privacy Policy &nbsp;|&nbsp; Terms &amp; Conditions &nbsp;|&nbsp; Cookie Policy</div>

</body>
</html>
```